Consulting Company Business Card

I am looking for a minimalist, classy, professional design on my business card. I would like it to be double-sided. I want to use the font and color scheme of my logo which are attached. Please be creative in the designs that you send me. I want to play off the design of my logo with the inner C that is Green and Blue broken up with the white.
Target Market(s)
Small Businesses
Industry/Entity Type
Consulting
Contact Information for Business Card
Dale M. Whitcombe, CPA CGMA, 555-014-2873, dwhitcombe@vorantaadvisory.example, www.vorantaadvisory.example

```html
<!DOCTYPE html>
<html lang="en">
<head>
<meta charset="utf-8">
<title>Voranta Advisory – Business Card</title>
<link href="https://fonts.googleapis.com/css2?family=Montserrat:wght@600;700&family=Arimo:wght@400&display=swap" rel="stylesheet">
<style>
  :root {
    --navy: #213259;
    --teal: #1e7f80;
    --white: #ffffff;
    --stage: #a3a3a3;
    --rule: #8a8a8a;
  }
  html, body {
    margin: 0;
    padding: 0;
    width: 1200px;
    height: 1200px;
    overflow: hidden;
    background: var(--stage);
  }
  .canvas {
    position: relative;
    width: 1200px;
    height: 1200px;
  }
  .card {
    position: absolute;
    top: 303px;
    height: 594px;
    overflow: hidden;
  }
  .card-back {
    left: 200px;
    width: 370px;
    background: var(--navy);
  }
  .card-front {
    left: 599px;
    width: 364px;
    background: var(--white);
  }

  /* back side */
  .back-disc {
    position: absolute;
    left: 50%;
    top: 170px;
    width: 240px;
    height: 240px;
    margin-left: -120px;
    border-radius: 50%;
    background: var(--teal);
  }
  .back-brand {
    position: absolute;
    left: 0;
    right: 0;
    top: 440px;
    text-align: center;
    font-family: "Montserrat", sans-serif;
    font-weight: 700;
    color: var(--white);
    letter-spacing: 0.08em;
    font-size: 26px;
    line-height: 1.2;
  }
  .back-web {
    position: absolute;
    left: 0;
    right: 0;
    top: 534px;
    text-align: center;
    font-family: "Arimo", sans-serif;
    font-size: 16px;
    color: var(--white);
    letter-spacing: 0.01em;
  }

  /* front side */
  .brand-mark {
    position: absolute;
    left: 50%;
    top: 66px;
    width: 100px;
    height: 100px;
    margin-left: -50px;
    border-radius: 50%;
    background: var(--navy);
  }
  .brand-name {
    position: absolute;
    left: 0;
    right: 0;
    top: 194px;
    text-align: center;
    font-family: "Montserrat", sans-serif;
    font-weight: 700;
    color: var(--navy);
    line-height: 1;
  }
  .brand-name .primary {
    display: block;
    font-size: 46px;
    letter-spacing: 0.02em;
  }
  .brand-name .secondary {
    display: block;
    margin-top: 10px;
    font-size: 16px;
    letter-spacing: 0.32em;
  }
  .person {
    position: absolute;
    left: 0;
    right: 0;
    top: 372px;
    text-align: center;
  }
  .person-name {
    font-family: "Montserrat", sans-serif;
    font-weight: 600;
    font-size: 23px;
    color: var(--navy);
    letter-spacing: 0.01em;
    margin: 0;
  }
  .person-title {
    font-family: "Arimo", sans-serif;
    font-size: 17px;
    color: var(--teal);
    margin: 6px 0 0;
    letter-spacing: 0.03em;
  }
  .icon-row {
    position: absolute;
    left: 0;
    right: 0;
    top: 740px;
    top: 438px;
    display: flex;
    justify-content: center;
    align-items: center;
    gap: 4px;
  }
  .icon-row .rule {
    width: 52px;
    height: 1px;
    background: var(--rule);
    margin: 0 4px;
  }
  .icon {
    width: 25px;
    height: 25px;
    border-radius: 3px;
    background: var(--navy);
    display: flex;
    align-items: center;
    justify-content: center;
  }
  .contact {
    position: absolute;
    left: 0;
    right: 0;
    top: 474px;
    text-align: center;
    font-family: "Arimo", sans-serif;
    font-size: 16px;
    line-height: 22px;
    color: var(--navy);
  }
  .contact p { margin: 0; }
</style>
</head>
<body>
<div class="canvas">

  <section class="card card-back" aria-label="Card back">
    <div class="back-disc"></div>
    <div class="back-brand">VORANTA<br>ADVISORY</div>
    <div class="back-web">www.vorantaadvisory.example</div>
  </section>

  <section class="card card-front" aria-label="Card front">
    <div class="brand-mark"></div>
    <div class="brand-name">
      <span class="primary">VORANTA</span>
      <span class="secondary">ADVISORY</span>
    </div>

    <div class="person">
      <p class="person-name">DALE M. WHITCOMBE</p>
      <p class="person-title">CPA CGMA</p>
    </div>

    <div class="icon-row">
      <span class="rule"></span>
      <span class="icon" aria-label="Phone">
        <svg width="15" height="15" viewBox="0 0 24 24" fill="#ffffff">
          <path d="M6.6 10.8a15.1 15.1 0 0 0 6.6 6.6l2.2-2.2a1 1 0 0 1 1-.25 11.4 11.4 0 0 0 3.6.57 1 1 0 0 1 1 1V20a1 1 0 0 1-1 1A17 17 0 0 1 3 4a1 1 0 0 1 1-1h3.5a1 1 0 0 1 1 1c0 1.25.2 2.45.57 3.57a1 1 0 0 1-.25 1z"/>
        </svg>
      </span>
      <span class="icon" aria-label="Email">
        <svg width="16" height="12" viewBox="0 0 24 18" fill="none" stroke="#ffffff" stroke-width="1.8">
          <rect x="1" y="1" width="22" height="16"/>
          <path d="M1 1l11 9 11-9M1 17l8-7M23 17l-8-7"/>
        </svg>
      </span>
      <span class="icon" aria-label="Website">
        <svg width="15" height="15" viewBox="0 0 24 24" fill="none" stroke="#ffffff" stroke-width="1.8">
          <circle cx="12" cy="12" r="10"/>
          <ellipse cx="12" cy="12" rx="4.5" ry="10"/>
          <path d="M2 12h20"/>
        </svg>
      </span>
      <span class="rule"></span>
    </div>

    <div class="contact">
      <p>555-014-2873</p>
      <p>dwhitcombe@vorantaadvisory.example</p>
      <p>www.vorantaadvisory.example</p>
    </div>
  </section>

</div>
</body>
</html>
```